Opening Soon Hoarding Design for Retail Footwear Chain

TREVALLO is a retail footwear chain operating primarily in North America. It offers exclusive and non-exclusive brands for men and women.

We need an advertisement design announcing a store opening, to be placed on a hoarding.

A hoarding is a large board in an enclosed shopping center, used to display advertisements; similar to a billboard. It is a temporary board (or fence) erected in front of a retail site during the construction period.

The advertisement we need is to be placed on the hoarding that covers the store front facade during the construction period, and it is removed the night prior to opening day.

Attached are the TREVALLO store pictures, as well as the logo / pantone color document. The primary colors identifying TREVALLO are Rose gold, white, and red.

The objective or focus of the advertisement on the hoarding should include the following:
- TREVALLO (as per logo)
- Opening soon
- website : www.trevallo-example.ca
- Facebook / Twitter
- A clearly identified section of the advertisement announcing that we are recruiting / looking for employees; this should be announced as: "Join the Trevallo Family" and provide email: careers@trevallo-example.ca

Target Market(s)

Women & men between the approx ages of 25 to 65. The age group is quite wide because the product range we have in the store is very diverse too.

Industry/Entity Type

Retail

Requirements
Must have
• 1- Trevallo name / logo
• 2- Opening soon
• 3- website: www.trevallo-example.ca (& Facebook / twitter reference)
• 4- Join the Trevallo Family: careers@trevallo-example.ca
• Main objective: To have a design that will intrigue people walking in a shopping mall enough for them to stop for a second and look at the ad design. (At the end of the day, that's the main objective of a hoarding design - to get people's attention).
Nice to have
• I can give you an approx. SIZE, but I would like a design that can be slightly modified for printing purposes, as the hoarding size from 1 store to the next will not be identical. However, I would like to use the same design for all hoardings.
• With that said, the approx hoarding size would be 15 feet wide and 10 feet high.
• Some other hoardings will be slightly bigger in width (going up to 20 ft max) but the height should be fairly standard.
Should not have
• The end design should not have a picture / design of the store as per the attached images. The store design and how it looks should be a surprise for the customers.

```html
<!DOCTYPE html>
<html lang="en">
<head>
<meta charset="utf-8">
<title>Trevallo – Opening Soon Hoarding</title>
<link rel="stylesheet" href="https://fonts.googleapis.com/css2?family=Archivo+Black&family=Michroma&family=Open+Sans:wght@600;700&display=swap">
<style>
  :root {
    --brand-red: #a30006;
    --brand-red-deep: #7e0004;
    --rose-gold: #e2b04a;
    --rose-gold-light: #f6d98a;
    --text-red: #9c0a0e;
    --paper: #ffffff;
    --pattern-tone: #e4cfcf;
  }
  * { margin: 0; padding: 0; box-sizing: border-box; }
  html, body {
    width: 1200px;
    height: 817px;
    overflow: hidden;
    background: var(--paper);
  }
  .hoarding {
    position: relative;
    width: 1200px;
    height: 817px;
    background: var(--paper);
    overflow: hidden;
    font-family: "Open Sans", Arial, sans-serif;
  }
  .backdrop-pattern {
    position: absolute;
    top: 400px;
    width: 330px;
    height: 417px;
    opacity: 0.55;
  }
  .backdrop-pattern--left {
    left: 0;
    background: radial-gradient(ellipse at 30% 40%, var(--pattern-tone) 0%, rgba(255,255,255,0) 70%);
  }
  .backdrop-pattern--right {
    right: 0;
    background: radial-gradient(ellipse at 70% 50%, var(--pattern-tone) 0%, rgba(255,255,255,0) 70%);
  }
  .header-band {
    position: absolute;
    top: 0;
    left: 0;
    width: 1200px;
    height: 400px;
  }
  .brand-name {
    position: absolute;
    top: 130px;
    left: 0;
    width: 1200px;
    padding-left: 28px;
    text-align: center;
    font-family: "Michroma", Arial, sans-serif;
    font-size: 66px;
    font-weight: 400;
    letter-spacing: 28px;
    color: var(--paper);
    line-height: 80px;
  }
  .headline {
    position: absolute;
    top: 412px;
    left: 0;
    width: 1200px;
    text-align: center;
    font-family: "Archivo Black", Impact, sans-serif;
    font-size: 90px;
    font-weight: 400;
    line-height: 110px;
    letter-spacing: -1px;
    color: var(--brand-red);
  }
  .contact-list {
    position: absolute;
    top: 527px;
    left: 384px;
    list-style: none;
  }
  .contact-item {
    display: flex;
    align-items: center;
    height: 59px;
    font-size: 30px;
    font-weight: 700;
    color: var(--text-red);
  }
  .contact-icon {
    flex: 0 0 auto;
    width: 34px;
    height: 34px;
    margin-right: 22px;
    background: var(--text-red);
  }
  .contact-icon--round { border-radius: 50%; }
  .recruit-banner {
    position: absolute;
    top: 732px;
    left: 172px;
    width: 856px;
    height: 43px;
    display: flex;
    align-items: center;
    justify-content: center;
    background: linear-gradient(90deg, rgba(163,0,6,0) 0%, var(--brand-red) 12%, var(--brand-red) 88%, rgba(163,0,6,0) 100%);
    color: var(--paper);
    font-size: 21.5px;
    font-weight: 600;
  }
</style>
</head>
<body>
<main class="hoarding">
  <div class="backdrop-pattern backdrop-pattern--left" role="img" aria-label="Faint interlocking rounded-square pattern in soft rose tones"></div>
  <div class="backdrop-pattern backdrop-pattern--right" role="img" aria-label="Faint interlocking rounded-square pattern in soft rose tones"></div>

  <svg class="header-band" viewBox="0 0 1200 400" aria-hidden="true">
    <defs>
      <linearGradient id="redField" x1="0" y1="0" x2="0" y2="1">
        <stop offset="0" stop-color="#b0000a"/>
        <stop offset="1" stop-color="#8e0005"/>
      </linearGradient>
      <linearGradient id="goldLine" gradientUnits="userSpaceOnUse" x1="0" y1="0" x2="1200" y2="0">
        <stop offset="0" stop-color="#c98a2a"/>
        <stop offset="0.5" stop-color="#f6d98a"/>
        <stop offset="1" stop-color="#c98a2a"/>
      </linearGradient>
      <linearGradient id="goldLineV" gradientUnits="userSpaceOnUse" x1="0" y1="0" x2="0" y2="380">
        <stop offset="0" stop-color="#c98a2a"/>
        <stop offset="0.5" stop-color="#f6d98a"/>
        <stop offset="1" stop-color="#c98a2a"/>
      </linearGradient>
    </defs>
    <path d="M0 0 H1200 V385 C1050 360 900 318 700 322 C480 326 300 345 120 350 C70 352 30 354 0 356 Z" fill="url(#redField)"/>
    <g class="gold-grid" stroke-width="4">
      <line x1="46" y1="0" x2="46" y2="354" stroke="url(#goldLineV)"/>
      <line x1="140" y1="0" x2="140" y2="349" stroke="url(#goldLineV)"/>
      <line x1="1055" y1="0" x2="1055" y2="359" stroke="url(#goldLineV)"/>
      <line x1="1148" y1="0" x2="1148" y2="376" stroke="url(#goldLineV)"/>
      <line x1="0" y1="68" x2="1200" y2="68" stroke="url(#goldLine)"/>
      <line x1="0" y1="254" x2="1200" y2="254" stroke="url(#goldLine)"/>
    </g>
    <path d="M0 356 C30 354 70 352 120 350 C300 345 480 326 700 322 C900 318 1050 360 1200 385" fill="none" stroke="url(#goldLine)" stroke-width="5"/>
  </svg>

  <h1 class="brand-name">TREVALLO</h1>

  <h2 class="headline">OPENING SOON</h2>

  <ul class="contact-list">
    <li class="contact-item"><span class="contact-icon contact-icon--round"></span>www.trevallo-example.ca</li>
    <li class="contact-item"><span class="contact-icon contact-icon--round"></span>#trevallo</li>
    <li class="contact-item"><span class="contact-icon"></span>social.trevallo-example.ca</li>
  </ul>

  <p class="recruit-banner">Join the Trevallo Family, email resume to: careers@trevallo-example.ca</p>
</main>
</body>
</html>
```